Leadership Brenvale Brochure Design*

We host a local leadership development program every two years. We need a brochure to promote the program. We would like it to be 8 1/2 x 11, tri-fold. I have attached a Word document with the necessary info for the brochure. The brochure will be professionally printed. We would like the final design to be in InDesign.

Target Market(s)

Potential participants of our leadership program. They will be local leaders, male and female, from 30-60 years of age.

Requirements
Must have
• Content as detailed in the Word document attached. Our logo.
Nice to have
• A design that is attractive to young professionals.

```html
<!DOCTYPE html>
<html lang="en">
<head>
<meta charset="utf-8">
<title>Leadership Brenvale – Tri-fold Brochure</title>
<link rel="stylesheet" href="https://fonts.googleapis.com/css2?family=Montserrat:wght@500;600;700;800&family=Open+Sans:wght@400;600;700&display=swap">
<style>
:root{
  --navy:#2c2a72;
  --navy-deep:#1f1d5a;
  --orange:#f39a1f;
  --ink:#2b2b3a;
  --muted:#6b6b78;
  --paper:#ffffff;
  --stage:#e9e9ec;
  --ghost:#e3e3ea;
}
*{box-sizing:border-box;margin:0;padding:0}
html,body{width:1200px;height:2392px;overflow:hidden;background:var(--stage)}
body{position:relative;font-family:"Open Sans",Arial,sans-serif;color:var(--ink)}
h1,h2,h3,h4{font-family:"Montserrat",Arial,sans-serif}

.cover-wrap{position:absolute;left:474px;top:36px;width:252px;height:584px;box-shadow:0 6px 18px rgba(0,0,0,.12)}
.cover-wrap .panel{transform:scale(.7);transform-origin:0 0}

.spread{position:absolute;left:60px;width:1080px;height:834px;display:flex;background:var(--paper);box-shadow:0 6px 18px rgba(0,0,0,.12)}
.spread.inside{top:660px}
.spread.outside{top:1530px}
.panel{position:relative;width:360px;height:834px;overflow:hidden;background:var(--paper)}
.panel + .panel{border-left:1px solid #efeff3}
.shapes{position:absolute;inset:0;width:100%;height:100%}

/* cover */
.cover-tagline{position:absolute;right:14px;top:24px;writing-mode:vertical-rl;font-family:"Montserrat",sans-serif;font-weight:600;font-size:15px;color:#9a9aa8;letter-spacing:.5px;line-height:1.3}
.quote-mark{font-family:"Montserrat",sans-serif;font-weight:800;color:var(--orange);font-size:64px;line-height:1}
.cover .quote-mark{position:absolute;left:26px;top:150px}
.cover-quote{position:absolute;left:26px;top:212px;width:170px;font-family:"Montserrat",sans-serif;font-weight:700;font-size:17px;line-height:1.3;color:var(--navy)}
.sponsors{position:absolute;left:26px;top:470px;width:180px;font-size:12px;line-height:1.4}
.sponsors .label{color:var(--muted);margin-bottom:8px}
.sponsors strong{display:block;color:var(--navy);font-family:"Montserrat",sans-serif;font-size:13px;margin-bottom:10px}
.cover-rule{position:absolute;left:26px;right:26px;top:700px;border-top:1px solid #d7d7e0}
.brand{position:absolute;display:flex;align-items:center;gap:8px;font-family:"Montserrat",sans-serif;font-weight:700;color:var(--navy)}
.brand .dot{width:22px;height:22px;border-radius:50%;background:var(--orange)}
.cover .brand{right:26px;top:740px;font-size:16px}

/* inside */
.photo{position:absolute;display:block}
.overview .photo{left:0;top:0;width:360px;height:300px;background:linear-gradient(135deg,#c98a52,#7d6a8f 55%,#3e4d7a)}
.overview .quote-mark{position:absolute;left:28px;top:318px;font-size:54px}
.overview-body{position:absolute;left:28px;right:28px;top:380px}
.section-title{font-size:22px;font-weight:800;color:var(--navy);margin-bottom:12px}
.copy{font-size:11px;line-height:1.6;color:var(--ink)}
.copy + .copy{margin-top:10px}
.bullets{list-style:none;margin-top:12px}
.bullets li{position:relative;padding-left:16px;font-size:11px;line-height:1.5;margin-bottom:8px}
.bullets li::before{content:"";position:absolute;left:0;top:5px;width:7px;height:7px;background:var(--orange)}

.schedule-head{position:absolute;left:28px;top:40px;background:var(--orange);color:#fff;font-family:"Montserrat",sans-serif;font-weight:800;font-size:22px;padding:6px 18px}
.ghost-title{position:absolute;right:-6px;top:20px;writing-mode:vertical-rl;font-family:"Montserrat",sans-serif;font-weight:800;font-size:54px;color:var(--ghost);letter-spacing:1px;white-space:nowrap}
.sessions{position:absolute;left:28px;width:240px}
.schedule .sessions{top:100px}
.details .sessions{top:44px;width:280px}
.session{margin-bottom:22px}
.session h3{font-size:17px;font-weight:800;color:var(--navy);line-height:1.2}
.session h4{font-size:12px;font-weight:600;color:var(--ink);margin-top:3px}
.session .time{font-size:12px;font-weight:700;color:var(--orange);margin:3px 0 5px}
.session ul{list-style:none}
.session li{font-size:10px;line-height:1.5;color:var(--muted);padding-left:10px;position:relative}
.session li::before{content:"–";position:absolute;left:0}
.schedule .photo{left:0;bottom:0;width:360px;height:210px;background:linear-gradient(160deg,#5b4fa0,#2c2a72)}

/* outside */
.about{background:var(--navy)}
.about-body{position:absolute;left:30px;right:30px;top:60px;color:#fff}
.about-body h2{color:var(--orange);font-size:22px;font-weight:800;margin-bottom:14px}
.about-body h3{color:var(--orange);font-size:15px;font-weight:700;margin:20px 0 8px}
.about-body .copy{color:#e6e6f2}
.alumni-body{position:absolute;left:28px;right:28px;top:54px}
.alumni-body h2{font-size:19px;font-weight:800;color:var(--navy);line-height:1.25;margin-bottom:18px}
.testimonial{display:flex;gap:14px;margin-bottom:26px}
.testimonial .photo{position:static;flex:0 0 92px;height:112px;background:linear-gradient(160deg,#b9b4ae,#6e6a68)}
.testimonial .copy{font-size:10.5px}
.attribution{font-size:10px;font-weight:700;color:var(--navy);margin-top:6px}
</style>
</head>
<body>

<!-- front cover (folded) -->
<div class="cover-wrap">
  <section class="panel cover">
    <svg class="shapes" viewBox="0 0 360 834" preserveAspectRatio="none" aria-hidden="true">
      <polygon points="150,0 250,0 150,190" fill="#2c2a72"/>
      <polygon points="250,0 360,0 360,640 205,360" fill="#f39a1f"/>
      <polygon points="300,560 360,500 360,660" fill="#2c2a72"/>
    </svg>
    <p class="cover-tagline">A Leadership<br>Development Program</p>
    <div class="quote-mark">“</div>
    <p class="cover-quote">The greatest asset of a community lies not in the amount of its treasure, but in the quality of its leadership.</p>
    <div class="sponsors">
      <p class="label">Sponsored by</p>
      <strong>Ridgeline Community College</strong>
      <strong>Brenvale Chamber of Commerce and Tourism</strong>
    </div>
    <div class="cover-rule"></div>
    <div class="brand"><span class="dot"></span>Leadership Brenvale</div>
  </section>
</div>

<!-- inside spread -->
<div class="spread inside">
  <section class="panel overview">
    <div class="photo" role="img" aria-label="Group photo of program participants"></div>
    <div class="quote-mark">“</div>
    <div class="overview-body">
      <h2 class="section-title">Program Overview</h2>
      <p class="copy">Leadership Brenvale is a leadership development program held every two years for current and emerging leaders in our community. Through a series of monthly sessions, participants learn how local business, government and service organizations work together.</p>
      <p class="copy">Each class builds lasting connections among people who care about the future of the region.</p>
      <ul class="bullets">
        <li>Meet the leaders shaping local industry and public life</li>
        <li>Build skills in teamwork, vision and communication</li>
        <li>Explore how community decisions are made</li>
        <li>Join a growing network of engaged alumni</li>
      </ul>
    </div>
  </section>

  <section class="panel schedule">
    <svg class="shapes" viewBox="0 0 360 834" preserveAspectRatio="none" aria-hidden="true">
      <polygon points="0,0 120,0 0,110" fill="#2c2a72"/>
    </svg>
    <div class="ghost-title">Leadership Brenvale</div>
    <h2 class="schedule-head">Schedule</h2>
    <div class="sessions">
      <div class="session">
        <h3>January 17</h3>
        <h4>Organizational Retreat &amp; Dinner (Attendance Mandatory)</h4>
        <p class="time">10:00 a.m. – 5:00 p.m.</p>
        <ul><li>Team building</li><li>Personal leadership styles</li><li>Welcome dinner</li></ul>
      </div>
      <div class="session">
        <h3>January 31</h3>
        <h4>Business &amp; Industry</h4>
        <p class="time">8:30 a.m. – 4:00 p.m.</p>
        <ul><li>Tour of local manufacturers</li><li>Economic development panel</li><li>Workforce trends</li></ul>
      </div>
      <div class="session">
        <h3>February 21</h3>
        <h4>Tourism</h4>
        <p class="time">8:30 a.m. – 4:00 p.m.</p>
        <ul><li>Visit regional attractions</li><li>Hospitality leaders panel</li></ul>
      </div>
    </div>
    <div class="photo" role="img" aria-label="Photo of participants at a session"></div>
  </section>

  <section class="panel details">
    <svg class="shapes" viewBox="0 0 360 834" preserveAspectRatio="none" aria-hidden="true">
      <polygon points="360,600 360,834 150,834" fill="#f39a1f"/>
      <polygon points="360,720 360,834 250,834" fill="#2c2a72"/>
    </svg>
    <div class="sessions">
      <div class="session">
        <h3>March 14</h3>
        <h4>Local Technologies &amp; Communications</h4>
        <p class="time">8:30 a.m. – 4:00 p.m.</p>
        <ul><li>Local media and news</li><li>Broadband in the region</li><li>Emerging tech firms</li></ul>
      </div>
      <div class="session">
        <h3>April 4</h3>
        <h4>Government</h4>
        <p class="time">8:30 a.m. – 4:00 p.m.</p>
        <ul><li>City and county offices</li><li>Meet elected officials</li><li>Courthouse visit</li></ul>
      </div>
      <div class="session">
        <h3>May 2</h3>
        <h4>Health &amp; Wellness</h4>
        <p class="time">8:30 a.m. – 4:00 p.m.</p>
        <ul><li>Tour of the regional hospital</li><li>Community health services</li><li>Wellness programs</li></ul>
      </div>
      <div class="session">
        <h3>May 16</h3>
        <h4>Graduation Ceremony and Luncheon</h4>
        <p class="time">11:30 a.m.</p>
        <ul><li>Class project presentations</li><li>Family and sponsors welcome</li></ul>
      </div>
    </div>
  </section>
</div>

<!-- outside spread -->
<div class="spread outside">
  <section class="panel about">
    <div class="about-body">
      <h2>Leadership Brenvale</h2>
      <p class="copy">Leadership Brenvale has prepared local leaders for more than two decades. Graduates serve on boards, lead businesses and give their time to causes across the region.</p>
      <p class="copy">The program is open to anyone who lives or works in the county and wants to make a difference.</p>
      <h3>Tuition</h3>
      <p class="copy">Tuition covers all sessions, meals and materials. Many employers sponsor their staff, and partial scholarships are available.</p>
      <h3>To Apply</h3>
      <p class="copy">Complete the application form and return it to the Chamber office by the deadline. Class size is limited.</p>
      <p class="copy">Brenvale Chamber of Commerce<br>100 Main Street, Brenvale<br>(555) 010-2400</p>
    </div>
  </section>

  <section class="panel alumni">
    <div class="alumni-body">
      <h2>What Community Alumni are saying</h2>
      <div class="testimonial">
        <div class="photo" role="img" aria-label="Portrait of an alumna"></div>
        <div>
          <p class="copy">“This program opened doors I did not know existed. I met people from every part of our community and learned how much we can do together.”</p>
          <p class="attribution">Class Graduate, 2016</p>
        </div>
      </div>
      <div class="testimonial">
        <div class="photo" role="img" aria-label="Portrait of an alumnus"></div>
        <div>
          <p class="copy">“Every session showed me a new side of our hometown. I left with friends, ideas and a real plan to give back.”</p>
          <p class="attribution">Class Graduate, 2018</p>
        </div>
      </div>
      <p class="copy">Ask any graduate and you will hear the same thing: the people you meet make the experience worth every hour.</p>
    </div>
  </section>

  <section class="panel cover">
    <svg class="shapes" viewBox="0 0 360 834" preserveAspectRatio="none" aria-hidden="true">
      <polygon points="150,0 250,0 150,190" fill="#2c2a72"/>
      <polygon points="250,0 360,0 360,640 205,360" fill="#f39a1f"/>
      <polygon points="300,560 360,500 360,660" fill="#2c2a72"/>
    </svg>
    <p class="cover-tagline">A Leadership<br>Development Program</p>
    <div class="quote-mark">“</div>
    <p class="cover-quote">The greatest asset of a community lies not in the amount of its treasure, but in the quality of its leadership.</p>
    <div class="sponsors">
      <p class="label">Sponsored by</p>
      <strong>Ridgeline Community College</strong>
      <strong>Brenvale Chamber of Commerce and Tourism</strong>
    </div>
    <div class="cover-rule"></div>
    <div class="brand"><span class="dot"></span>Leadership Brenvale</div>
  </section>
</div>

</body>
</html>
```